Harrowby Lending Hard Money Lender

We are looking for this flyer to be redesigned. We would like it to be even more simple than the attached design. No photos, no exclamation points, a 3-4 color palate maximum. We would do not want any graphics around the "Harrowby Lending" logo.

```html
<!DOCTYPE html>
<html lang="en">
<head>
<meta charset="utf-8">
<title>Harrowby Lending – Hard Money Loans Flyer</title>
<link rel="stylesheet" href="https://fonts.googleapis.com/css2?family=Source+Sans+3:ital,wght@0,400;0,700;1,400;1,700&display=swap">
<style>
  :root {
    --brand-blue: #134d8b;
    --accent-red: #d22128;
    --ink: #1c2a3f;
    --tint: #e7edf6;
    --paper: #ffffff;
    --backdrop: #ffffff;
  }
  * { margin: 0; padding: 0; box-sizing: border-box; }
  html, body {
    width: 1200px; height: 1200px; overflow: hidden;
    background: var(--backdrop);
    font-family: "Source Sans 3", "Myriad Pro", Arial, sans-serif;
    color: var(--ink);
  }
  .flyer {
    position: absolute; left: 256px; top: 153px;
    width: 696px; height: 901px;
    background: var(--paper);
    overflow: hidden;
  }
  .brand {
    position: absolute; left: 0; right: 0; top: 95px;
    text-align: center;
    font-size: 46px; font-weight: 400; letter-spacing: 2px;
    color: var(--brand-blue);
    line-height: 1;
  }
  .headline-band {
    position: absolute; left: 0; top: 239px; width: 100%; height: 153px;
    background: var(--brand-blue); color: var(--paper); text-align: center;
  }
  .headline-band h1 {
    font-weight: 400; font-size: 68px; line-height: 1;
    margin-top: 25px; letter-spacing: 0.5px;
  }
  .headline-band .rate { font-size: 24px; margin-top: 12px; }
  .arrows { position: absolute; left: 0; top: 430px; }
  .loan-types {
    position: absolute; left: 264px; top: 425px;
    list-style: none; font-weight: 700; font-size: 33px; line-height: 41px;
  }
  .perks {
    position: absolute; left: 264px; top: 572px;
    list-style: none; font-style: italic; font-size: 19px; line-height: 23px;
  }
  .perks strong { font-weight: 700; }
  .contact-band {
    position: absolute; left: 0; top: 709px; width: 100%; height: 192px;
    background: var(--tint);
  }
  .phone {
    position: absolute; left: 166px; top: 678px; width: 364px; height: 63px;
    background: var(--brand-blue); color: var(--paper);
    font-size: 45px; font-weight: 700; text-align: center; line-height: 63px;
  }
  .web-line {
    position: absolute; left: 81px; width: 532px; top: 762px;
    display: flex; justify-content: space-between; align-items: center;
    font-size: 24px;
  }
  .address-line {
    position: absolute; left: 81px; width: 532px; top: 806px;
    display: flex; justify-content: space-between; font-size: 15.5px;
  }
</style>
</head>
<body>
  <main class="flyer">
    <div class="brand">HARROWBY LENDING</div>

    <section class="headline-band">
      <h1>Hard Money Loans</h1>
      <p class="rate">Rates From 8%</p>
    </section>

    <svg class="arrows" width="250" height="90" viewBox="0 0 250 90" aria-hidden="true">
      <g fill="var(--accent-red)">
        <rect x="0" y="0" width="234" height="4"/>
        <polygon points="226,0 241,0 228,9 224,4"/>
        <rect x="0" y="38" width="234" height="4"/>
        <polygon points="226,38 241,38 228,47 224,42"/>
        <rect x="0" y="77" width="234" height="4"/>
        <polygon points="226,77 241,77 228,86 224,81"/>
      </g>
    </svg>

    <ul class="loan-types">
      <li>Fix &amp; Flip Loans</li>
      <li>Commercial Loans</li>
      <li>Hard Money Loans</li>
    </ul>

    <ul class="perks">
      <li><strong>Same-Day</strong> Approval</li>
      <li><strong>No</strong> Processing, Appraisal, or Extra Fees</li>
      <li><strong>100% Financing</strong> (w/ Additional Collateral)*</li>
    </ul>

    <div class="contact-band"></div>
    <div class="phone">303.555.0142</div>
    <div class="web-line">
      <span>hello@harrowbylending.com</span>
      <span>•</span>
      <span>harrowbylending.com</span>
    </div>
    <div class="address-line">
      <span>1840 Alder Ridge Blvd., Suite 100</span>
      <span>Denver, CO 80219</span>
    </div>
  </main>
</body>
</html>
```